Direct to Consumer extended service contract business with a new disruptive business model needs a

We need a customized wordpress design for a company called 'Bright Harbor Assurance'.
We provide an innovative and unique service contract protection program direct to consumers. This program provides monthly coverage for all electronics purchased in the last 4 years and all electronics the consumer purchases in the future for a low monthly fee. The overall design should communicate a sense of legitimacy, ethics, and superior customer service and support (in an industry that has a huge PR issue to overcome).
Electronics is the first product group, other product groups with different price points to launch in the future..

Target Market(s)

All purchasers of electronic goods...all demographics

Industry/Entity Type

Electronics

Font styles to use
Sans Serif

Requirements
Must have
• Customer Testimonials
Industry News
Customer ratings
Blog posts
Call to action messaging
Like the functional elements and design of veltomarket.example (need to be better)
Nice to have
• Like to see video testimonials
Social network "whats trending related to electronics or service contract industry"
Easy way to register products for warranty

```html
<!DOCTYPE html>
<html lang="en">
<head>
<meta charset="utf-8">
<title>Bright Harbor Assurance</title>
<link href="https://fonts.googleapis.com/css2?family=Raleway:wght@400;500;600;700&family=Open+Sans:wght@400;600;700&display=swap" rel="stylesheet">
<style>
:root{
  --green:#3aa54a;
  --green-dark:#2f8f3e;
  --ink:#3d3d3d;
  --text:#555;
  --muted:#888;
  --charcoal:#4a4a4a;
  --pattern:#eceeec;
  --line:#dcdcdc;
  --field:#e6e6e6;
  --white:#fff;
}
*{box-sizing:border-box;margin:0;padding:0}
html,body{width:1200px;height:1107px;overflow:hidden;background:var(--white)}
body{position:relative;font-family:"Open Sans",Arial,sans-serif;color:var(--text);font-size:7px}
.abs{position:absolute}
.heading{font-family:"Raleway",Arial,sans-serif;font-weight:600;color:var(--ink);text-transform:uppercase;text-align:center}
.heading em{font-style:normal;color:var(--green)}
.sub{font-family:"Raleway",Arial,sans-serif;color:var(--text);text-align:center;line-height:1.55}
.pattern{background:var(--pattern)}
.photo{background:linear-gradient(135deg,#c9d3dc,#8d9aa6)}

/* left page */
.topbar{left:0;top:0;width:467px;height:11px;background:var(--green);color:#fff;font-size:5.5px;line-height:11px;padding:0 7px;display:flex;justify-content:space-between}
.topbar span{margin-right:6px}
.header{left:0;top:11px;width:467px;height:31px;border-bottom:1px solid var(--line)}
.brand{left:77px;top:8px;display:flex;align-items:center;gap:5px;font-family:"Raleway",sans-serif;font-weight:700;color:var(--green);font-size:8px;line-height:1;width:110px}
.brand i{width:12px;height:12px;background:var(--green);display:block;flex:none}
.nav{left:226px;top:13px;display:flex;font-size:6px;color:var(--ink)}
.nav span{padding:0 6px;border-left:1px solid var(--line)}
.nav span:first-child{border:0}
.hero{left:0;top:42px;width:467px;height:180px}
.bubble{border-radius:50%;background:#fff;box-shadow:0 1px 3px rgba(0,0,0,.2);text-align:center;font-family:"Raleway",sans-serif;color:var(--ink)}
.bubble small{display:block;font-size:5.5px;margin-top:12px}
.bubble b{font-size:14px;font-weight:700}
.bubble.main{background:var(--green);color:#fff;border:4px solid #fff}
.bubble.main small{font-size:9px;margin-top:22px;line-height:1.2}
.bubble.main b{font-size:20px}
.hero-title{left:0;top:184px;width:467px;text-align:center;font-family:"Raleway",sans-serif;font-weight:700;color:var(--green);font-size:10px}
.hero-text{left:85px;top:197px;width:297px;text-align:center;font-size:6.3px;line-height:1.45}
.join{left:0;top:228px;width:467px;height:30px;background:linear-gradient(#fafafa,#eee);border-top:1px solid var(--line);border-bottom:1px solid var(--line)}
.join p{position:absolute;left:93px;top:9px;font-family:"Raleway",sans-serif;font-weight:600;font-size:10px;color:var(--ink)}
.join p em{font-style:normal;color:var(--green)}
.btn{background:var(--green);color:#fff;text-align:center;font-family:"Raleway",sans-serif}
.join .btn{position:absolute;left:294px;top:5px;width:82px;height:19px;line-height:19px;font-size:8px}
.feature{top:278px;width:82px}
.feature .icon{width:60px;height:60px;border-radius:50%;display:flex;align-items:center;justify-content:center}
.icon.g{background:var(--green)} .icon.d{background:var(--charcoal)}
.feature h4{font-family:"Raleway",sans-serif;font-weight:700;color:var(--green);font-size:7.5px;margin-top:13px;line-height:1}
.feature h5{font-weight:400;font-size:5.5px;text-transform:uppercase;color:var(--ink)}
.feature ul{list-style:none;margin-top:4px}
.feature li{font-size:4.6px;line-height:7px;padding-left:7px;position:relative}
.feature li:before{content:"✓";position:absolute;left:0;color:var(--green)}
.divider{height:1px;background:var(--line)}
.testi-card{left:87px;top:509px;width:293px;height:71px;background:#fff;box-shadow:0 0 3px rgba(0,0,0,.12)}
.avatar{left:96px;top:489px;width:46px;height:46px;border-radius:50%;background:linear-gradient(#d8d8d8,#a9a9a9);border:3px solid #fff;box-shadow:0 0 2px rgba(0,0,0,.25)}
.testi-name{left:148px;top:513px;font-family:"Raleway",sans-serif;font-weight:600;color:var(--green);font-size:11px}
.testi-role{left:149px;top:526px;font-size:5.5px;color:var(--ink)}
.testi-text{left:97px;top:542px;width:160px;font-size:5.3px;line-height:1.4}
.video{left:264px;top:513px;width:110px;height:61px;background:linear-gradient(135deg,#8a7d73,#4f5a66)}
.dots{display:flex;gap:3px}
.dots i{width:16px;height:2px;background:#e3e3e3;display:block}
.dots i.on{background:var(--green)}
.tweet-band{left:0;top:625px;width:467px;height:147px}
.tweet-frame{left:100px;top:647px;width:264px;height:109px;border:3px solid #d3d5d3;background:rgba(255,255,255,.35)}
.tweet-mark{left:222px;top:635px;width:22px;height:22px;border-radius:50%;background:var(--green)}
.tweet-text{left:120px;top:673px;width:224px;text-align:center;font-size:6px;line-height:1.65;color:var(--ink)}
.tweet-time{left:120px;top:707px;width:224px;text-align:center;font-size:5.5px;color:var(--green)}
.plan{color:#fff;text-align:center;font-family:Arial,sans-serif}
.plan .title{font-size:15px;height:34px;line-height:34px}
.plan .price{background:#fff;color:var(--ink);font-size:15px;font-weight:700;height:30px;line-height:30px}
.plan .price sup,.plan .price small{font-size:6px;font-weight:400}
.plan .price.gn{color:var(--green)}
.plan ul{list-style:none;font-size:5.5px}
.plan li{height:17px;line-height:17px}
.plan li.mark{font-size:10px}
.plan .cta{display:inline-block;background:#fff;color:var(--ink);font-size:5.5px;line-height:1.4;padding:3px 9px;margin-top:4px}
.plan.dark{background:var(--charcoal)}
.plan.dark .title{background:var(--charcoal);border-bottom:1px solid #666}
.plan.hot{background:var(--green)}
.plan.hot .title{font-size:16px}
.plan.hot ul{padding-top:4px}
.plan.hot li{height:20px;line-height:20px}
.plan.hot .cta{padding:4px 10px;margin-top:6px}

/* right page */
.news-item{width:202px;font-size:6.2px;line-height:1.55}
.news-item h6{font-family:"Raleway",sans-serif;font-weight:600;color:var(--green);font-size:5.5px;text-transform:uppercase}
.news-item .date{color:var(--muted);font-size:5.5px}
.news-item .more{color:var(--green);font-size:5.5px;font-weight:600}
.news-item.r{text-align:right}
.tl-line{left:875px;top:136px;width:2px;height:300px;background:#d0d0d0}
.tl-dot{width:12px;height:12px;border-radius:50%;background:var(--charcoal);border:2px solid #fff;box-shadow:0 0 0 1px #ccc}
.rated{left:563px;top:481px;width:624px;height:158px}
.rating{width:170px;text-align:center}
.rating .stars{display:flex;justify-content:center;gap:2px}
.rating h5{font-size:8px;font-weight:600;color:var(--ink);margin-top:4px}
.rating p{font-size:7.5px}
.rating p b{color:var(--ink)}
.rating a{display:block;color:var(--green);font-size:8px;font-weight:600;margin-top:5px;text-decoration:none}
.contact-band{left:563px;top:742px;width:624px;height:236px}
.form{left:742px;top:794px;width:266px;height:184px;background:#fff;border-top:2px solid var(--green)}
.field{position:absolute;left:13px;width:240px;height:18px;background:var(--field);border:1px solid #d8d8d8;color:#999;font-size:6px;text-align:center;line-height:16px}
.submit{left:106px;top:138px;width:55px;height:17px;line-height:17px;font-size:7px;font-weight:700}
.base-rule{left:563px;top:977px;width:624px;height:4px;background:var(--green)}
.connect{left:563px;top:1001px;width:624px;text-align:center;font-family:"Raleway",sans-serif;font-size:10px;color:var(--ink)}
.socials{left:563px;top:1018px;width:624px;display:flex;justify-content:center;gap:12px}
.socials i{width:19px;height:19px;border-radius:50%;background:var(--ink);display:block}
.copy{left:663px;top:1056px;width:424px;text-align:center;font-size:5.5px;line-height:1.6;color:var(--muted)}
</style>
</head>
<body>

<!-- ===== Home page, upper half ===== -->
<div class="abs topbar"><div><span>About Us</span><span>Blog</span><span>Support</span></div><div><span>Language</span><span>English ▾</span><span>Login/Register</span></div></div>
<header class="abs header">
  <div class="abs brand"><i></i><span>Bright Harbor Assurance</span></div>
  <nav class="abs nav"><span>Home</span><span>Services</span><span>Pricing</span><span>Clientele</span><span>Contact</span></nav>
</header>

<section class="abs hero pattern" role="img" aria-label="Light grey pattern of scattered electronics outlines"></section>
<svg class="abs" style="left:0;top:42px" width="467" height="180" aria-hidden="true">
  <g fill="none" stroke="#888" stroke-width="1">
    <path d="M160 95 Q165 120 190 122"/><path d="M310 40 Q285 30 262 45"/><path d="M300 130 Q292 145 272 140"/><path d="M150 60 Q160 45 185 50"/>
  </g>
</svg>
<div class="abs bubble" style="left:104px;top:50px;width:66px;height:66px"><small>TV Protection</small><b>$100</b></div>
<div class="abs bubble" style="left:312px;top:44px;width:70px;height:70px"><small>Phone Protection</small><b>$100</b></div>
<div class="abs bubble" style="left:286px;top:115px;width:64px;height:64px"><small>Fridge Protection</small><b>$100</b></div>
<div class="abs bubble main" style="left:172px;top:50px;width:122px;height:122px"><small>Multiple Products<br>for a price of</small><b>19.99</b><br><span style="font-size:7px">per month</span></div>
<svg class="abs" style="left:0;top:42px" width="467" height="180" aria-hidden="true">
  <g fill="#3aa54a" font-family="Raleway,sans-serif" font-weight="700" font-size="13">
    <text x="123" y="76">?</text><text x="349" y="80">?</text><text x="318" y="128">?</text>
  </g>
</svg>
<div class="abs hero-title">BRIGHT HARBOR ASSURANCE</div>
<p class="abs hero-text">provides one contract or plan for all the electronics products you purchased in the last 2 years and all products you purchase in the future for a low monthly fee.</p>

<section class="abs join"><p>JOIN <em>BRIGHT HARBOR ASSURANCE</em> NOW!</p><div class="btn">SIGNUP</div></section>

<div class="abs feature" style="left:74px">
  <div class="icon g"><svg width="30" height="30" viewBox="0 0 30 30" fill="none" stroke="#fff" stroke-width="1.6"><path d="M3 15 Q15 1 27 15 Z"/><path d="M15 15v9q0 3-3 2"/></svg></div>
  <h4>SUPERIOR</h4><h5>Coverage</h5>
  <ul><li>One plan covers all electronics</li><li>Thousands of eligible products</li><li>Register any brand from any retailer</li></ul>
</div>
<div class="abs feature" style="left:161px">
  <div class="icon d"><svg width="26" height="28" viewBox="0 0 26 28" fill="none" stroke="#fff" stroke-width="1.6"><rect x="4" y="12" width="18" height="14"/><path d="M8 12V7a5 5 0 0 1 10 0v5"/></svg></div>
  <h4>REVOLUTIONARY</h4><h5>Protection</h5>
  <ul><li>Repair, Replace or Refund</li><li>Cover past, present and future purchases</li><li>Coverage never ends</li></ul>
</div>
<div class="abs feature" style="left:244px">
  <div class="icon g"><svg width="30" height="30" viewBox="0 0 30 30" fill="none" stroke="#fff" stroke-width="1.6"><circle cx="15" cy="15" r="12"/><path d="M10 9l3 0 1 4-2 1q2 4 5 5l1-2 4 1 0 3q-9 1-12-12z"/></svg></div>
  <h4>HASSLE FREE</h4><h5>Customer Service</h5>
  <ul><li>24 hr customer Hotline</li><li>Over 10,000 service centers</li><li>No questions asked</li></ul>
</div>
<div class="abs feature" style="left:326px">
  <div class="icon d"><svg width="28" height="28" viewBox="0 0 28 28" fill="none" stroke="#fff" stroke-width="1.8"><path d="M8 4v14M4 14l4 4 4-4M20 24V10M16 14l4-4 4 4"/></svg></div>
  <h4>COMPETITOR</h4><h5>Comparison</h5>
  <ul><li>24 hr customer Hotline</li><li>Over 10,000 service centers</li><li>No questions asked</li></ul>
</div>

<div class="abs divider" style="left:74px;top:413px;width:320px"></div>

<h2 class="abs heading" style="left:0;top:431px;width:467px;font-size:12.5px">Customer <em>Testimonials</em></h2>
<p class="abs sub" style="left:95px;top:448px;width:277px;font-size:6.3px">Real stories from real customers who really broke stuff.Real stories from real customers who really broke stuff.Real stories from real customers who really broke stuff.</p>

<svg class="abs" style="left:71px;top:532px" width="10" height="16" aria-hidden="true"><path d="M8 1L2 8l6 7" fill="none" stroke="#3aa54a" stroke-width="2"/></svg>
<svg class="abs" style="left:386px;top:532px" width="10" height="16" aria-hidden="true"><path d="M2 1l6 7-6 7" fill="none" stroke="#3aa54a" stroke-width="2"/></svg>
<div class="abs testi-card"></div>
<div class="abs avatar" role="img" aria-label="Customer portrait"></div>
<div class="abs testi-name">DANIEL MARLOW</div>
<div class="abs testi-role">Manager, <span style="color:var(--muted)">Northfield Supply</span></div>
<p class="abs testi-text">Lorem ipsum dolor sit amet, consectetur adipiscing elit, of Quisque ultricies vestibulum molestie. Graphic Design the power of Suspendisse ultricies Graphic Design the power of Suspendisse potent</p>
<div class="abs video" role="img" aria-label="Video testimonial thumbnail showing a group call"></div>
<svg class="abs" style="left:311px;top:536px" width="16" height="14" aria-hidden="true"><rect width="16" height="14" rx="3" fill="#222"/><path d="M6 4l5 3-5 3z" fill="#fff"/></svg>
<div class="abs dots" style="left:209px;top:588px"><i></i><i class="on"></i><i></i></div>

<section class="abs tweet-band pattern" role="img" aria-label="Light grey pattern of scattered electronics outlines"></section>
<div class="abs tweet-frame"></div>
<div class="abs tweet-mark"></div>
<p class="abs tweet-text">Accounting's responsiveness is better than any other @industry professional I've ever seen. Whether it's picking up the phone and calling you back or email response. They are very @responsive.</p>
<div class="abs tweet-time">2 DaysBefore</div>
<div class="abs dots" style="left:209px;top:741px"><i></i><i class="on"></i><i></i></div>

<h2 class="abs heading" style="left:0;top:805px;width:467px;font-size:12.5px">Our <em>Latest Plans</em></h2>
<p class="abs sub" style="left:95px;top:822px;width:277px;font-size:6.3px">Real stories from real customers who really broke stuff.Real stories from real customers who really broke stuff.Real stories from real customers who really broke stuff.</p>

<div class="abs plan dark" style="left:81px;top:884px;width:83px;height:175px">
  <div class="title">Basic</div><div class="price gn"><sup>$</sup>19.99<small>/mon.</small></div>
  <ul><li>50MB Monthly Traffic</li><li>3 Email Account</li><li class="mark">✖</li><li>Theme Updates</li><li>Layered Design Files</li></ul>
  <span class="cta">Sign Up Now</span>
</div>
<div class="abs plan hot" style="left:187px;top:863px;width:94px;height:216px">
  <div class="title">Standard</div><div class="price"><sup>$</sup>45<small>/mon.</small></div>
  <ul><li>150MB Monthly Traffic</li><li>10 Email Account</li><li class="mark">✔</li><li>Theme Updates</li><li>Layered Design Files</li></ul>
  <span class="cta">Sign Up Now</span>
</div>
<div class="abs plan dark" style="left:292px;top:884px;width:95px;height:175px">
  <div class="title">Premium</div><div class="price gn"><sup>$</sup>75<small>/mon.</small></div>
  <ul><li>300MB Monthly Traffic</li><li>15 Email Account</li><li class="mark">✔</li><li>Theme Updates</li><li>Layered Design Files</li></ul>
  <span class="cta">Sign Up Now</span>
</div>

<!-- ===== Home page, lower half ===== -->
<div class="abs divider" style="left:660px;top:22px;width:430px;background:#eee"></div>
<h2 class="abs heading" style="left:563px;top:60px;width:624px;font-size:15px">News <em>Feed</em></h2>
<p class="abs sub" style="left:690px;top:83px;width:370px;font-size:7.3px">Real stories from real customers who really broke stuff.Real stories from real customers who really broke stuff.Real stories from real customers who really broke stuff.</p>

<div class="abs tl-line"></div>
<div class="abs tl-dot" style="left:870px;top:171px"></div>
<div class="abs tl-dot" style="left:870px;top:274px"></div>
<div class="abs tl-dot" style="left:870px;top:377px"></div>

<article class="abs news-item r" style="left:658px;top:148px">
  <h6>There are many variations of passages</h6><div class="date">05/18/2014</div>
  <p>Lorem Ipsum is simply dummy text of the printing and typesetting by the readable content of a page when looking at its layout and calling you back. They are very responsive.</p>
  <div class="more">READ MORE</div>
</article>
<div class="abs photo" style="left:890px;top:136px;width:202px;height:82px" role="img" aria-label="Businessman working at a laptop in a bright office"></div>

<div class="abs photo" style="left:658px;top:239px;width:201px;height:83px;background:linear-gradient(135deg,#6b5446,#1f1a17)" role="img" aria-label="Cup of coffee on a glass table"></div>
<article class="abs news-item" style="left:890px;top:251px">
  <h6>There are many variations of passages</h6><div class="date">05/18/2014</div>
  <p>Lorem Ipsum is simply dummy text of the printing and typesetting by the readable content of a page when looking at its layout and calling you back. They are very responsive.</p>
  <div class="more">READ MORE</div>
</article>

<article class="abs news-item r" style="left:658px;top:355px">
  <h6>There are many variations of passages</h6><div class="date">05/18/2014</div>
  <p>Lorem Ipsum is simply dummy text of the printing and typesetting by the readable content of a page when looking at its layout and calling you back. They are very responsive.</p>
  <div class="more">READ MORE</div>
</article>
<div class="abs photo" style="left:890px;top:342px;width:202px;height:83px;background:linear-gradient(135deg,#d9dde2,#7b8fa3)" role="img" aria-label="Hand pointing at a computer screen"></div>

<section class="abs rated pattern" role="img" aria-label="Light grey pattern of scattered electronics outlines"></section>
<h2 class="abs heading" style="left:563px;top:500px;width:624px;font-size:14.5px">Rated #1 <em>by the people: our customers.</em></h2>
<svg width="0" height="0" style="position:absolute" aria-hidden="true"><defs>
  <symbol id="star" viewBox="0 0 20 20"><path d="M10 1l2.7 6 6.3.6-4.8 4.3 1.4 6.4L10 15l-5.6 3.3 1.4-6.4L1 7.6 7.3 7z"/></symbol>
  <linearGradient id="half"><stop offset="50%" stop-color="#3aa54a"/><stop offset="50%" stop-color="#111"/></linearGradient>
</defs></svg>
<div class="abs rating" style="left:649px;top:549px">
  <div class="stars"><svg width="20" height="20" fill="#3aa54a"><use href="#star"/></svg><svg width="20" height="20" fill="#3aa54a"><use href="#star"/></svg><svg width="20" height="20" fill="#3aa54a"><use href="#star"/></svg><svg width="20" height="20" fill="#3aa54a"><use href="#star"/></svg><svg width="20" height="20" fill="url(#half)"><use href="#star"/></svg></div>
  <h5>Orchard App Market</h5><p>4.5 average on 7000+ reviews</p><a>Read More</a>
</div>
<div class="abs rating" style="left:789px;top:549px">
  <div class="stars"><svg width="20" height="20" fill="#3aa54a"><use href="#star"/></svg><svg width="20" height="20" fill="#3aa54a"><use href="#star"/></svg><svg width="20" height="20" fill="#3aa54a"><use href="#star"/></svg><svg width="20" height="20" fill="#3aa54a"><use href="#star"/></svg><svg width="20" height="20" fill="url(#half)"><use href="#star"/></svg></div>
  <h5>Riverline App Shop</h5><p><b>4.5</b> average on <b>7000+</b> reviews</p><a>Read More</a>
</div>
<div class="abs rating" style="left:937px;top:549px">
  <div class="stars"><svg width="20" height="20" fill="#3aa54a"><use href="#star"/></svg><svg width="20" height="20" fill="#3aa54a"><use href="#star"/></svg><svg width="20" height="20" fill="#3aa54a"><use href="#star"/></svg><svg width="20" height="20" fill="#3aa54a"><use href="#star"/></svg><svg width="20" height="20" fill="url(#half)"><use href="#star"/></svg></div>
  <h5>Lumen Play Hub</h5><p><b>4.5</b> average on <b>7000+</b> reviews</p><a>Read More</a>
</div>

<h2 class="abs heading" style="left:563px;top:671px;width:624px;font-size:15px">Contact <em>Us</em></h2>
<p class="abs sub" style="left:690px;top:696px;width:370px;font-size:7.3px">Real stories from real customers who really broke stuff.Real stories from real customers who really broke stuff.Real stories from real customers who really broke stuff.</p>

<section class="abs contact-band pattern" role="img" aria-label="Light grey pattern of scattered electronics outlines"></section>
<form class="abs form">
  <div class="field" style="top:21px">Name</div>
  <div class="field" style="top:48px">Email</div>
  <div class="field" style="top:75px;height:73px">Message</div>
  <div class="abs btn submit">SUBMIT</div>
</form>
<div class="abs base-rule"></div>

<footer>
  <div class="abs connect">Connect with BHA</div>
  <div class="abs socials"><i></i><i></i><i></i><i></i><i></i><i></i><i></i></div>
  <p class="abs copy">Copyright © 2014 Bright Harbor Assurance. All rights reserved.<br><span style="display:block;margin-top:4px">Lorem Ipsum is simply dummy text of the printing and typesetting industry. Lorem Ipsum has been the industry's standard dummy text ever since publishing software like Verso of Lorem Ipsum.</span></p>
</footer>

</body>
</html>
```